Criação de Papelaria Profissional para Construção & Engenharia
A empresa queria:
" Empresa de 28 anos, muito centrada no nome FALUCENA que é o sobrenome do dono da empresa e maior diferencial no mercado, a experiência! A empresa preza pela qualidade no atendimento ao cliente, sendo que o ponto forte é estar junto ao cliente em todas as etapas do projeto, principalmente durante a obra "

```html
<!DOCTYPE html>
<html lang="pt-BR">
<head>
<meta charset="UTF-8">
<title>FALUCENA – Cartão de Visita</title>
<link rel="stylesheet" href="https://fonts.googleapis.com/css2?family=Montserrat:wght@300;400;600;700&display=swap">
<style>
  :root {
    --canvas: #e9e9ea;
    --card: #ffffff;
    --red: #b3151b;
    --band-grey: #c9c9cb;
    --ink: #4a4a4a;
    --ink-soft: #6b6b6b;
    --logo-grey: #7a7a7c;
    --mark-dark: #3a3a3a;
    --soft-shape: #f1f1f2;
  }
  * { box-sizing: border-box; margin: 0; padding: 0; }
  html, body { width: 1200px; height: 1200px; overflow: hidden; }
  body {
    background: var(--canvas);
    font-family: "Montserrat", sans-serif;
    display: flex;
    flex-direction: column;
    align-items: center;
    justify-content: center;
    gap: 60px;
  }
  .card {
    position: relative;
    width: 900px;
    height: 514px;
    background: var(--card);
    box-shadow: 0 10px 30px rgba(0,0,0,.12);
    overflow: hidden;
  }
  .card__band {
    position: absolute;
    left: 0; right: 0; bottom: 0;
    height: 16px;
    display: flex;
  }
  .card__band .band-red { background: var(--red); }
  .card__band .band-grey { background: var(--band-grey); flex: 1; }

  /* front */
  .card--front .card__band .band-red { width: 57%; }
  .contact-block {
    position: absolute;
    left: 70px; top: 150px;
  }
  .person {
    border-left: 6px solid var(--red);
    padding-left: 14px;
    margin-bottom: 26px;
  }
  .person__name {
    font-weight: 700;
    color: var(--red);
    font-size: 28px;
    letter-spacing: .5px;
    line-height: 1.1;
  }
  .person__role {
    font-weight: 400;
    color: var(--ink-soft);
    font-size: 20px;
    margin-top: 4px;
  }
  .contact-list { list-style: none; }
  .contact-list li {
    display: flex;
    align-items: flex-start;
    gap: 14px;
    font-size: 18px;
    color: var(--ink);
    line-height: 1.2;
    margin-bottom: 12px;
  }
  .contact-list svg { flex: none; width: 24px; height: 24px; }
  .logo {
    display: flex;
    align-items: center;
    gap: 12px;
  }
  .logo__square { background: var(--mark-dark); }
  .logo__name {
    font-weight: 300;
    color: var(--logo-grey);
    letter-spacing: 3px;
  }
  .card--front .logo {
    position: absolute;
    right: 90px; top: 195px;
  }
  .card--front .logo__square { width: 34px; height: 34px; }
  .card--front .logo__name { font-size: 46px; }

  /* back */
  .card--back .card__band .band-red { width: 62%; }
  .backdrop {
    position: absolute;
    left: 220px; top: 40px;
    width: 520px; height: 300px;
    background: linear-gradient(180deg, var(--soft-shape), rgba(241,241,242,0));
  }
  .card--back .logo {
    position: absolute;
    left: 50%; top: 50%;
    transform: translate(-50%, -60%);
  }
  .card--back .logo__square { width: 56px; height: 56px; }
  .card--back .logo__name { font-size: 84px; letter-spacing: 5px; }
</style>
</head>
<body>

<section class="card card--front" aria-label="Frente do cartão">
  <div class="contact-block">
    <div class="person">
      <p class="person__name">NOME E SOBRENOME</p>
      <p class="person__role">Cargo | Função</p>
    </div>
    <ul class="contact-list">
      <li>
        <svg viewBox="0 0 24 24"><circle cx="12" cy="12" r="12" fill="var(--red)"/><path d="M8.5 6.5l2 2.2-1.2 1.4c.8 1.7 2 2.9 3.6 3.7l1.4-1.2 2.2 2-1.2 1.8c-3.9-.3-7.8-4.2-8.1-8.1z" fill="#fff"/></svg>
        <span>(00) 0000-0000</span>
      </li>
      <li>
        <svg viewBox="0 0 24 24"><circle cx="12" cy="12" r="12" fill="var(--red)"/><rect x="6.5" y="8" width="11" height="8" fill="#fff"/><path d="M6.5 8l5.5 4.5L17.5 8" fill="none" stroke="var(--red)" stroke-width="1.2"/></svg>
        <span>contato@exemplo.com</span>
      </li>
      <li>
        <svg viewBox="0 0 24 24"><circle cx="12" cy="12" r="12" fill="var(--red)"/><circle cx="12" cy="12" r="5.5" fill="none" stroke="#fff" stroke-width="1.4"/><path d="M6.5 12h11M12 6.5c-2.5 3-2.5 8 0 11M12 6.5c2.5 3 2.5 8 0 11" fill="none" stroke="#fff" stroke-width="1.1"/></svg>
        <span>www.exemplo.com.br</span>
      </li>
      <li>
        <svg viewBox="0 0 24 24"><circle cx="12" cy="12" r="12" fill="var(--red)"/><path d="M12 18s-4.5-4.6-4.5-7.5a4.5 4.5 0 019 0C16.5 13.4 12 18 12 18z" fill="#fff"/><circle cx="12" cy="10.5" r="1.6" fill="var(--red)"/></svg>
        <span>rua exemplo, sl 000<br>cidade-UF, CEP: 00000-000</span>
      </li>
    </ul>
  </div>
  <div class="logo">
    <span class="logo__square"></span>
    <span class="logo__name">FALUCENA</span>
  </div>
  <div class="card__band"><span class="band-red"></span><span class="band-grey"></span></div>
</section>

<section class="card card--back" aria-label="Verso do cartão">
  <div class="backdrop" role="img" aria-label="Silhuetas claras de edifícios ao fundo"></div>
  <div class="logo">
    <span class="logo__square"></span>
    <span class="logo__name">FALUCENA</span>
  </div>
  <div class="card__band"><span class="band-red"></span><span class="band-grey"></span></div>
</section>

</body>
</html>
```